Rosa Belle Christmas Open House

Rosa Belle is a small gift boutique. We carry a very eclectic mix of fun products: women's apparel, jewelry, handbags, candles, stationery, etc. We have our annual Christmas Open House on Friday, November 7th and Saturday, November 8th. I usually use a graphic from Wavy Fern Studio so I love the look of her art. I want the postcard to be standard size and would love a whimsical Christmas feeling. Nothing traditional. I prefer bright, fun colors or softer pastels as opposed to traditional red and green. No Santas... But I do love snowflakes, presents, reindeer, fun trees, etc.

During those 2 days, customers will receive 20% off their purchase of $20 or more. When they spend $75, they'll receive a free Shop Nearby tote. I've attached the image for you to use in small format for my customers to see.

Target Market(s)

Women ages 18-55

Industry/Entity Type

Boutique

Font styles to use
Serif
Script

Colors
add136
33b7a4
f58f94
f04a50
8869ae
85acd3
85cae6
ffcf3e
f59296

Requirements
Must have
• A Christmas feel. Snowflakes, presents, glitter. I love a playful, scripty font.
Nice to have
• Love whimsical designs- I've included images of designs I really like.
Should not have
• Nothing traditional. No red and green

```html
<!DOCTYPE html>
<html lang="en">
<head>
<meta charset="utf-8">
<title>Rosa Belle Christmas Open House Postcard</title>
<link rel="stylesheet" href="https://fonts.googleapis.com/css2?family=Great+Vibes&family=Dancing+Script:wght@400;500&display=swap">
<style>
  :root {
    --backdrop: #2c2c2c;
    --paper: #ffffff;
    --pink: #f59296;
    --red: #f04a50;
    --teal: #33b7a4;
    --purple: #8869ae;
    --purple-deep: #5b3c8a;
    --yellow: #ffcf3e;
    --ink: #1e1a1c;
    --line: #222222;
  }
  html, body {
    margin: 0;
    padding: 0;
    width: 821px;
    height: 1200px;
    overflow: hidden;
    background: var(--backdrop);
  }
  .canvas {
    position: relative;
    width: 821px;
    height: 1200px;
  }
  .postcard {
    position: absolute;
    left: 60px;
    width: 707px;
    background: var(--paper);
    box-shadow: 0 4px 14px rgba(0,0,0,0.5);
  }
  .postcard--front { top: 33px; height: 547px; }
  .postcard--back { top: 612px; height: 550px; }
  .postcard svg { display: block; }

  .script-title { font-family: "Great Vibes", cursive; }
  .script-body { font-family: "Dancing Script", cursive; }

  .front-brand { fill: var(--red); font-size: 74px; }
  .front-headline { fill: var(--ink); font-size: 62px; }

  .back-brand { fill: var(--paper); font-size: 42px; }
  .back-copy { fill: var(--ink); font-size: 23px; }
  .back-dates { fill: var(--purple-deep); font-size: 23px; }
  .offer-main { fill: var(--paper); font-size: 19px; font-weight: 500; }
  .offer-small { fill: var(--paper); font-size: 11px; }
  .tote-main { fill: var(--purple-deep); font-size: 27px; }
  .tote-small { fill: var(--purple); font-size: 12px; }
</style>
</head>
<body>
<main class="canvas">

  <!-- Front of postcard -->
  <section class="postcard postcard--front">
    <svg width="707" height="547" viewBox="0 0 707 547">
      <defs>
        <linearGradient id="tree-tones" x1="0" y1="0" x2="1" y2="1">
          <stop offset="0" stop-color="#6d8a5e"/>
          <stop offset="0.55" stop-color="#b9c77a"/>
          <stop offset="1" stop-color="#c23a3f"/>
        </linearGradient>
        <linearGradient id="bag-tones" x1="0" y1="0" x2="1" y2="1">
          <stop offset="0" stop-color="#9ccf5a"/>
          <stop offset="0.5" stop-color="#f3a0a6"/>
          <stop offset="1" stop-color="#ef7d2f"/>
        </linearGradient>
      </defs>

      <rect class="front-paper" width="707" height="547" fill="var(--paper)"/>

      <path class="tree-photo" role="img" aria-label="Photo of a decorated Christmas tree with baubles, stars and wrapped presents"
            d="M300,0 H707 V190 C640,262 530,312 430,302 C360,294 320,255 300,205 Z"
            fill="url(#tree-tones)"/>

      <path class="front-wave" d="M0,250 C120,232 240,278 330,302 C460,336 600,268 707,196 V547 H0 Z"
            fill="var(--pink)"/>

      <path class="front-swoosh" d="M268,190 C292,160 330,172 322,212 C334,286 472,322 600,282 C652,264 690,232 707,204"
            fill="none" stroke="var(--teal)" stroke-width="20" stroke-linecap="round"/>

      <path class="bags-photo" role="img" aria-label="Photo of colourful shopping bags and gift boxes"
            d="M362,547 C352,430 452,344 560,348 C628,350 680,380 707,408 V547 Z"
            fill="url(#bag-tones)"/>
      <path class="bags-arc" d="M366,545 C352,430 452,338 562,342 C630,346 676,372 700,396"
            fill="none" stroke="var(--yellow)" stroke-width="16" stroke-linecap="round"/>

      <text class="script-title front-brand" x="44" y="122">Rosa Belle</text>
      <text class="script-title front-headline" x="60" y="338">Annual</text>
      <text class="script-title front-headline" x="42" y="410">Christmas</text>
      <text class="script-title front-headline" x="20" y="482">Open House</text>
    </svg>
  </section>

  <!-- Back of postcard -->
  <section class="postcard postcard--back">
    <svg width="707" height="550" viewBox="0 0 707 550">
      <defs>
        <linearGradient id="gift-tones" x1="0" y1="0" x2="1" y2="1">
          <stop offset="0" stop-color="#d9dde0"/>
          <stop offset="0.5" stop-color="#d8453f"/>
          <stop offset="1" stop-color="#c9ccd2"/>
        </linearGradient>
      </defs>

      <rect class="back-paper" width="707" height="550" fill="var(--paper)"/>

      <path class="back-panel" d="M0,0 H255 C270,80 300,150 330,200 C420,255 462,330 442,420 C430,480 400,512 392,550 H0 Z"
            fill="var(--pink)"/>

      <path class="gift-photo" role="img" aria-label="Photo of silver and red wrapped gifts with baubles"
            d="M0,0 H255 C262,120 200,230 100,262 C60,272 20,270 0,266 Z"
            fill="url(#gift-tones)"/>

      <path class="yellow-swoosh" d="M2,330 C40,300 110,290 190,258 C230,240 250,220 262,200"
            fill="none" stroke="var(--yellow)" stroke-width="16" stroke-linecap="round"/>
      <path class="purple-rim" d="M0,272 C130,280 240,230 258,0"
            fill="none" stroke="var(--purple)" stroke-width="14"/>
      <path class="purple-swoosh" d="M240,212 C300,190 380,198 448,214"
            fill="none" stroke="var(--purple)" stroke-width="18" stroke-linecap="round"/>
      <path class="purple-curl" d="M330,202 C432,252 472,332 444,422 C424,482 362,498 300,490"
            fill="none" stroke="var(--purple)" stroke-width="18" stroke-linecap="round"/>

      <g class="offer-badge">
        <circle cx="305" cy="163" r="36" fill="var(--teal)"/>
        <text class="script-body offer-main" x="305" y="158" text-anchor="middle">20% off</text>
        <text class="script-body offer-small" x="305" y="172" text-anchor="middle">on purchase of</text>
        <text class="script-body offer-small" x="305" y="186" text-anchor="middle">$20 &amp; more</text>
      </g>

      <text class="script-title back-brand" x="268" y="258" text-anchor="middle">Rosa Belle</text>
      <text class="script-body back-copy" x="270" y="286" text-anchor="middle">is having</text>
      <text class="script-body back-copy" x="260" y="326" text-anchor="middle">Annual Christmas Open House</text>
      <text class="script-body back-copy" x="240" y="366" text-anchor="middle">on Friday &amp; Saturday,</text>
      <text class="script-body back-dates" x="230" y="402" text-anchor="middle">November 7th &amp; November 8th</text>

      <g class="tote-offer">
        <path d="M0,433 H208 A35,35 0 0 1 208,503 H0 Z" fill="var(--teal)"/>
        <text class="script-body tote-main" x="40" y="470">spend $75</text>
        <text class="script-body tote-small" x="14" y="491">&amp; receive a free Shop Nearby tote</text>
      </g>

      <rect class="tote-art" role="img" aria-label="Image of a canvas Shop Nearby tote bag"
            x="238" y="420" width="92" height="112" rx="6" fill="#e6e4df"/>

      <rect class="stamp-box" x="613" y="100" width="54" height="61" fill="none" stroke="var(--line)" stroke-width="1.5"/>
      <line class="address-line" x1="500" y1="301" x2="673" y2="301" stroke="var(--line)" stroke-width="1.2"/>
      <line class="address-line" x1="500" y1="328" x2="673" y2="328" stroke="var(--line)" stroke-width="1.2"/>
      <line class="address-line" x1="500" y1="355" x2="673" y2="355" stroke="var(--line)" stroke-width="1.2"/>
    </svg>
  </section>

</main>
</body>
</html>
```